Thank You Card

Catering company customer Thank You cards

Thank you card to past clients after event completion

Should be on recycled or green paper.

Room to write personal message. No long prewritten messages of thanks and gratitude.

Should have Red and Zapfino fonts to match logo

Simple bold design thanking international clientele

Design could incorporate fish, knives, fire, wine, wood

No palm trees, coconuts, surfboards,beachballs or tikis
Updates

1. Please show envelope designs that match the card. 

2. Thank you going down the left side of the card cover in a column in at least 5 languages: Mahalo, Japanese, Chinese, French, Spanish, German, Italian

Target Market(s)

Company based on Oahu servicing locals and visitors

Industry/Entity Type

Catering

```html
<!DOCTYPE html>
<html lang="en">
<head>
<meta charset="utf-8">
<title>Thank You Card and Envelope</title>
<link href="https://fonts.googleapis.com/css2?family=Italianno&family=Noto+Sans+JP:wght@400&family=Noto+Sans+KR:wght@400&family=Cormorant+Garamond:wght@500&display=swap" rel="stylesheet">
<style>
  :root {
    --brand-red: #c41f28;
    --script-red: #c4202a;
    --paper: #ffffff;
    --frame: #d98a8a;
    --flap-line: #e8a0a0;
  }
  html, body {
    margin: 0;
    padding: 0;
    width: 1200px;
    height: 1200px;
    overflow: hidden;
    background: var(--paper);
  }
  .canvas {
    position: relative;
    width: 1200px;
    height: 1200px;
  }

  /* Company name */
  .brand-name {
    position: absolute;
    display: flex;
    align-items: center;
    gap: 7px;
    color: var(--paper);
    font-family: "Cormorant Garamond", serif;
    font-weight: 500;
    white-space: nowrap;
  }
  .brand-name .brand-dot {
    width: 8px;
    height: 8px;
    background: var(--paper);
  }

  /* Card cover */
  .card {
    position: absolute;
    left: 290px;
    top: 12px;
    width: 660px;
    height: 718px;
    border: 1px solid var(--frame);
    box-sizing: border-box;
    background: var(--paper);
    overflow: hidden;
  }
  .card-band {
    position: absolute;
    left: 0;
    top: 6px;
    width: 100%;
    height: 52px;
    background: var(--brand-red);
  }
  .card .brand-name {
    left: 0;
    top: 6px;
    width: 100%;
    height: 52px;
    justify-content: center;
    font-size: 17px;
    letter-spacing: 1px;
  }
  .card-art {
    position: absolute;
    left: 160px;
    top: 70px;
    width: 500px;
    height: 510px;
    background: radial-gradient(ellipse at 70% 45%, rgba(196,31,40,0.55), rgba(230,120,120,0.3) 45%, rgba(255,255,255,0) 72%);
  }
  .languages {
    position: absolute;
    left: 28px;
    top: 392px;
    margin: 0;
    padding: 0;
    list-style: none;
    color: var(--script-red);
  }
  .languages li {
    font-family: "Italianno", cursive;
    font-size: 27px;
    line-height: 29px;
  }
  .languages li.cjk {
    font-family: "Noto Sans JP", sans-serif;
    font-size: 11px;
    line-height: 26px;
  }
  .languages li.cjk-zh {
    font-size: 13px;
  }
  .languages li.cjk-ko {
    font-family: "Noto Sans KR", sans-serif;
    font-size: 13px;
  }
  .thanks {
    position: absolute;
    margin: 0;
    font-family: "Italianno", cursive;
    font-weight: 400;
    color: var(--script-red);
    white-space: nowrap;
  }
  .card .thanks {
    left: 24px;
    top: 626px;
    font-size: 100px;
    line-height: 0.85;
  }

  /* Envelope */
  .envelope {
    position: absolute;
    left: 192px;
    top: 752px;
    width: 806px;
    height: 423px;
    overflow: hidden;
  }
  .envelope-flap {
    position: absolute;
    left: 0;
    top: 0;
  }
  .envelope .brand-name {
    left: 78px;
    top: 190px;
    width: 78px;
    flex-direction: column;
    gap: 6px;
    font-size: 13px;
    text-align: center;
  }
  .envelope .thanks {
    left: 200px;
    top: 184px;
    font-size: 76px;
    line-height: 0.85;
  }
  .envelope-art {
    position: absolute;
    left: 448px;
    top: 0;
    width: 358px;
    height: 340px;
    background: radial-gradient(ellipse at 85% 55%, rgba(210,70,60,0.6), rgba(235,140,130,0.3) 50%, rgba(255,255,255,0) 75%);
  }
</style>
</head>
<body>
<div class="canvas">

  <section class="card">
    <div class="card-band"></div>
    <div class="brand-name"><span class="brand-dot"></span>Koa Table</div>
    <div class="card-art" role="img" aria-label="Brush illustration of a school of red fish swimming down toward the lower left"></div>
    <ul class="languages">
      <li>Mahalo</li>
      <li>Danke</li>
      <li>Grazie</li>
      <li>Gracias</li>
      <li>Merci</li>
      <li class="cjk" lang="ja">ありがとうございます</li>
      <li class="cjk cjk-zh" lang="zh">谢谢</li>
      <li class="cjk cjk-ko" lang="ko">감사합니다</li>
    </ul>
    <h1 class="thanks">Thank You</h1>
  </section>

  <section class="envelope">
    <svg class="envelope-flap" width="160" height="423" viewBox="0 0 160 423">
      <path d="M22 0 H76 V423 H22 Q0 423 0 401 V22 Q0 0 22 0 Z" fill="var(--brand-red)"/>
      <line x1="77" y1="0" x2="77" y2="423" stroke="var(--flap-line)" stroke-width="2"/>
      <rect x="78" y="0" width="78" height="423" fill="var(--brand-red)"/>
    </svg>
    <div class="brand-name"><span class="brand-dot"></span>Koa Table</div>
    <h2 class="thanks">Thank You</h2>
    <div class="envelope-art" role="img" aria-label="Brush illustration of red fish swimming toward the left from the envelope edge"></div>
  </section>

</div>
</body>
</html>
```